Luxury Eco accommodation needs new website

Luxury lodge accommodation on exclusive private property in Flinders Ranges South Australia.
Brand new venture needs new site.
Focus on small group accommodation on exclusive property with outdoor experiences. Mountain biking , bush walking, outdoor dining.
We currently have a website but are having trouble making it our own. Needs to be "polished" by a professional.
Can you help?

www.larkhollowretreat.com.au

Target Market(s)

High income travellers, luxury accommodation

Industry/Entity Type

Accommodation

```html
<!DOCTYPE html>
<html lang="en">
<head>
<meta charset="utf-8">
<title>Lark Hollow Retreat – Luxury Lodge, Flinders Ranges</title>
<link href="https://fonts.googleapis.com/css2?family=Source+Sans+3:wght@400;600&family=Yanone+Kaffeesatz:wght@600&family=Rubik+Dirt&family=Open+Sans:wght@400&display=swap" rel="stylesheet">
<style>
:root{
  --nav-panel:rgba(150,150,150,.55);
  --nav-border:rgba(230,230,230,.7);
  --nav-text:#ffffff;
  --frame-tan:#c9a48a;
  --frame-inner:#ffffff;
  --logo-ink:#3c3f44;
  --hero-sky:#c9a27c;
  --hero-hill:#9a5a34;
  --hero-field:#6b4a2a;
  --hero-shade:#2e2418;
  --content-bg:#c7c7c7;
  --content-top:#f4f4f4;
  --card-bg:#e4e4e4;
  --card-edge:#ffffff;
  --tab-title:#ffffff;
  --body-text:#333333;
  --link-red:#b0121b;
  --field-border:#b9b9b9;
  --button:#7a7a7a;
  --footer-band:#7b7b7b;
  --footer-bottom:#bdbdbd;
  --social:#e8e8e8;
}
*{box-sizing:border-box;margin:0;padding:0}
html,body{width:1200px;height:1095px;overflow:hidden;background:#fff}
.canvas{position:relative;width:1200px;height:1095px;overflow:hidden;font-family:"Open Sans",sans-serif}

/* hero */
.hero{position:absolute;left:0;top:0;width:1200px;height:565px;
  background:
   radial-gradient(ellipse 420px 160px at 1000px 260px, rgba(230,160,90,.55), transparent 70%),
   linear-gradient(180deg,var(--hero-sky) 0%,var(--hero-hill) 22%,#8a6a44 45%,var(--hero-field) 70%,var(--hero-shade) 100%)}
.social{position:absolute;top:12px;left:868px;display:flex;gap:10px}
.social span{width:28px;height:28px;border-radius:5px;background:var(--social);opacity:.85}
.nav-panel{position:absolute;top:74px;height:53px;background:var(--nav-panel);border:1px solid var(--nav-border);border-radius:6px;display:flex;align-items:center}
.nav-left{left:143px;width:330px;padding-left:22px;gap:18px}
.nav-right{left:726px;width:327px;padding-left:38px;gap:18px}
.nav-panel a{color:var(--nav-text);text-decoration:none;font-family:"Source Sans 3",sans-serif;font-size:17px;text-transform:uppercase;letter-spacing:-.2px}
.dropdown{position:absolute;left:219px;top:134px;width:171px;height:99px;background:rgba(190,180,175,.6);border:1px solid rgba(230,230,230,.6);border-radius:6px;padding:10px 12px}
.dropdown a{display:block;color:#fff;text-decoration:none;font-family:"Source Sans 3",sans-serif;font-size:16px;line-height:27px}
.brand{position:absolute;left:465px;top:32px;width:269px;height:143px}
.brand svg{position:absolute;inset:0}
.brand-name{position:absolute;left:0;right:0;top:54px;text-align:center;font-family:"Source Sans 3",sans-serif;font-weight:400;font-size:22px;letter-spacing:4px;color:var(--logo-ink);line-height:30px}
.arrow{position:absolute;top:306px}
.arrow-prev{left:145px}.arrow-next{left:1028px}
.headline{position:absolute;font-family:"Rubik Dirt",sans-serif;color:#f2f2f2;font-size:29px;letter-spacing:1px;text-transform:uppercase;text-shadow:0 1px 3px rgba(0,0,0,.5);white-space:nowrap}
.headline-1{left:284px;top:402px}
.headline-2{left:543px;top:452px}
.pager{position:absolute;left:555px;top:532px;width:89px;height:27px;background:#c7a58a;display:flex;gap:6px;padding:7px 10px}
.pager span{width:13px;height:13px;background:#3b3b3b;color:#fff;font-size:9px;line-height:13px;text-align:center}
.pager span.active{background:#fff;color:#222}

/* content */
.content{position:absolute;left:0;top:565px;width:1200px;height:380px;background:linear-gradient(180deg,var(--content-top) 0,#d8d8d8 90px,var(--content-bg) 100%)}
.card{position:absolute;top:31px;width:255px;height:306px;background:linear-gradient(135deg,#f2f2f2,var(--card-bg) 60%,#d6d6d6);border:1px solid var(--card-edge);border-radius:3px;box-shadow:0 10px 12px -6px rgba(0,0,0,.35)}
.card-lodge{left:166px}.card-experiences{left:470px}.card-contact{left:778px}
.card-tab{position:absolute;left:14px;top:-8px;width:227px;height:52px}
.card-title{position:absolute;left:0;right:0;top:-4px;text-align:center;font-family:"Yanone Kaffeesatz",sans-serif;font-weight:600;font-size:24px;color:var(--tab-title);text-shadow:0 1px 2px rgba(0,0,0,.45)}
.card-photo{position:absolute;left:15px;top:50px;width:222px;height:114px}
.photo-lodge{background:linear-gradient(180deg,#6f94c4 0,#b8c8dc 35%,#8c8a7e 60%,#8a7b5c 100%)}
.photo-experiences{background:linear-gradient(180deg,#f0c8a8 0,#b8694c 35%,#6e3a30 60%,#5a3a30 100%)}
.card-text{position:absolute;left:15px;top:180px;width:228px;font-size:11.5px;line-height:16.3px;color:var(--body-text)}
.view-details{position:absolute;right:26px;top:278px;font-size:9px;letter-spacing:.8px;color:var(--link-red);text-decoration:none}
.view-details b{color:#888;font-weight:400}
.field{position:absolute;left:22px;width:215px;height:30px;border:1px solid var(--field-border);background:#f7f7f7;font-size:11px;letter-spacing:.8px;color:#9a9a9a;padding:7px 8px}
.send{position:absolute;left:87px;top:269px;width:85px;height:25px;background:var(--button);color:#fff;font-size:12px;text-align:center;line-height:25px}

/* footer */
.footer-nav{position:absolute;left:0;top:945px;width:1200px;height:110px;background:var(--footer-band);display:flex;justify-content:center;align-items:flex-start;padding-top:30px;gap:0}
.footer-nav a{color:#fff;text-decoration:none;font-family:"Source Sans 3",sans-serif;font-size:13px}
.footer-nav i{display:inline-block;width:8px;height:8px;border-radius:50%;background:#b3b3b3;margin:6px 19px 0}
.copyright{position:absolute;left:0;top:1055px;width:1200px;height:40px;background:var(--footer-bottom);text-align:center;font-size:9.5px;letter-spacing:.8px;line-height:40px;color:#222}
</style>
</head>
<body>
<div class="canvas">
  <header class="hero" role="img" aria-label="Photograph of two hikers walking through golden grassland towards a hillside lodge in the Flinders Ranges at sunset">
  </header>

  <div class="social">
    <span></span><span></span><span></span><span></span><span></span>
  </div>

  <nav class="nav-panel nav-left">
    <a href="#">Home</a><a href="#">Luxury Lodge</a><a href="#">Other Stays</a>
  </nav>
  <nav class="nav-panel nav-right">
    <a href="#">Experiences</a><a href="#">Gallery</a><a href="#">Contact</a>
  </nav>

  <div class="dropdown">
    <a href="#">- About the Lodge</a>
    <a href="#">- Accommodation</a>
    <a href="#">- Rates</a>
  </div>

  <div class="brand">
    <svg width="269" height="143" viewBox="0 0 269 143">
      <path d="M22 0H247L269 20V123L247 143H22L0 123V20Z" fill="var(--frame-tan)"/>
      <path d="M26 8H243L259 24V119L243 135H26L10 119V24Z" fill="var(--frame-inner)"/>
    </svg>
    <div class="brand-name">LARK HOLLOW<br>RETREAT</div>
  </div>

  <svg class="arrow arrow-prev" width="24" height="82" viewBox="0 0 24 82"><path d="M23 1L1 41L23 81" fill="none" stroke="#fff" stroke-width="1.5"/></svg>
  <svg class="arrow arrow-next" width="24" height="82" viewBox="0 0 24 82"><path d="M1 1L23 41L1 81" fill="none" stroke="#fff" stroke-width="1.5"/></svg>

  <div class="headline headline-1">Lark Hollow Lodge is nestled in the heart of</div>
  <div class="headline headline-2">SA’s magnificent Flinders Ranges</div>

  <div class="pager"><span class="active">1</span><span>2</span><span>3</span><span>4</span></div>

  <main class="content">
    <section class="card card-lodge">
      <svg class="card-tab" viewBox="0 0 227 52"><defs><linearGradient id="tabA" x1="0" y1="0" x2="0" y2="1"><stop offset="0" stop-color="#8c8c8c"/><stop offset="1" stop-color="#d9d9d9"/></linearGradient></defs><path d="M0 10Q4 0 16 2Q40 10 50 26Q70 48 113 48Q156 48 176 26Q186 10 211 2Q223 0 227 10L227 6Q220 -2 113 -2Q6 -2 0 6Z" fill="url(#tabA)"/><path d="M14 4Q40 10 50 26Q70 46 113 46Q156 46 176 26Q186 10 213 4Z" fill="url(#tabA)"/></svg>
      <h2 class="card-title">The Lodge</h2>
      <div class="card-photo photo-lodge" role="img" aria-label="Photograph of the lodge buildings on a grassy hilltop under a blue sky"></div>
      <p class="card-text">Lark Hollow Lodge is nestled in the heart of SA’s magnificent Flinders Ranges. It is located on Lark Hollow Retreat, 480 kms north of Adelaide and stretches along the northern boundary of the great Flinders Ranges National</p>
      <a class="view-details" href="#">View Details <b>→</b></a>
    </section>

    <section class="card card-experiences">
      <svg class="card-tab" viewBox="0 0 227 52"><path d="M14 4Q40 10 50 26Q70 46 113 46Q156 46 176 26Q186 10 213 4Z" fill="url(#tabA)"/></svg>
      <h2 class="card-title">Experiences</h2>
      <div class="card-photo photo-experiences" role="img" aria-label="Photograph of a small group of walkers looking out at rugged red mountain ridges"></div>
      <p class="card-text">Lorem Ipsum. Proin gravida nibh vel velit auctor aliquet. Aenean sollicitudin, lorem quis bibendum auctor, nisi elit consequat ipsum, nec sagittis sem nibh id elit. Duis sed odio sit amet nibh vulputate cursus a sit amet mauris.</p>
      <a class="view-details" href="#">View Details <b>→</b></a>
    </section>

    <section class="card card-contact">
      <svg class="card-tab" viewBox="0 0 227 52"><path d="M14 4Q40 10 50 26Q70 46 113 46Q156 46 176 26Q186 10 213 4Z" fill="url(#tabA)"/></svg>
      <h2 class="card-title">Quick Contact</h2>
      <div class="field" style="top:51px">Name..</div>
      <div class="field" style="top:89px">Tel..</div>
      <div class="field" style="top:124px">Email..</div>
      <div class="field" style="top:160px;height:102px">Message..</div>
      <div class="send">Send</div>
    </section>
  </main>

  <footer>
    <nav class="footer-nav">
      <a href="#">Home</a><i></i><a href="#">Luxury Lodge</a><i></i><a href="#">Other Stays</a><i></i><a href="#">Experiences</a><i></i><a href="#">Gallery</a><i></i><a href="#">Contact</a>
    </nav>
    <div class="copyright">Copyright © 2013 Lark Hollow Lodge. All right reserved</div>
  </footer>
</div>
</body>
</html>
```